Bold Vehicle Wrap Design for 2025 Halvorne Tundrix Cargo Van

We need a full wrap design for our 2025 Halvorne-Kestrel Tundrix 3100 High Roof Cargo Van. This van will be used to represent Brightwell Task Crew, and we want it to stand out with a bold, professional look.

Vehicle Details:
2025 Tundrix 3100
High Roof
144" Wheelbase
Cargo configuration (no windows)

Our current logo is black, white, and gray — but we’re open to more colorful wrap concepts that could even influence a logo recolor.

We want a wrap design that:
Looks bold and professional
Incorporates icons for the services we provide:Plumbing,Handyman, Land Management, Junk and Debris Removal
Incorporates or complements our current logo
Avoids placing critical text or graphics across sliding doors, seams, or complex panel curves
Download all project files (template, logo, reference images):
https://files.qorvashare-example.net/s/7kd2mq9vlt48xw1pzr6ub/QRTAKZmNcLwYPd3e8hxsuVB?key=5tqzm1wx7ch2jdp3ks9vle4nb&v=k7pwr2dz&dl=0

Target Market(s)

ocal residential and commercial customers in need of professional plumbing, handyman, land management, and junk/debris removal services. Homeowners and property managers looking for reliable and skilled service providers. Businesses and contractors who require prompt, professional, and trustworthy support for their facilities and properties. Customers who value quality workmanship and clear branding that conveys professionalism and expertise.

Industry/Entity Type

Local Service Providers specializing in residential and commercial property maintenance

Requirements
Must have
• Incorporate the Brightwell Task Crew logo with flexibility for adding color to complement the wrap. Use bold, professional, and eye-catching colors that stand out on the road. Include icons or visuals representing these key services: Plumbing Handyman Land Management Junk and Debris Removal. Design must fit a 2025 Halvorne Tundrix 3100 High Roof Cargo Van (144" WB, cargo version with sliding door) — avoid placing important graphics or text over the sliding door seams or complex curves. Use high-contrast text and graphics for maximum readability from a distance. Design should be modern and clean, but bold enough to be memorable. Wrap design must work on all visible sides: driver side, passenger side, rear, and front. Provide final deliverables in Adobe Illustrator (.ai) or Photoshop (.psd) with layered files.
Nice to have
• Mockup images showing the wrap applied to the van template.
Should not have
• Do not place important text, logos, or graphics across the sliding door seam or uneven panel curves — they may get distorted or hidden.No low-contrast text or graphics that make information hard to read from a distance.Do not include any unrelated images or icons that don’t represent Brightwell Task Crew’ core offerings.Do not create a design that looks too similar to competitors or other well-known brands. No fonts that are hard to read or too decorative for a work vehicle.

```html
<!DOCTYPE html>
<html lang="en">
<head>
<meta charset="utf-8">
<title>Brightwell Task Crew – Van Wrap Side Panel</title>
<link href="https://fonts.googleapis.com/css2?family=Montserrat:wght@500;600;800&display=swap" rel="stylesheet">
<style>
  :root {
    --navy: #1b3f6e;
    --navy-deep: #17365f;
    --orange: #df4227;
    --white: #ffffff;
    --backdrop: #0d0d0d;
  }
  html, body {
    margin: 0;
    padding: 0;
    width: 1125px;
    height: 1200px;
    overflow: hidden;
    background: var(--backdrop);
  }
  .canvas {
    position: relative;
    width: 1125px;
    height: 1200px;
    display: flex;
    align-items: center;
    justify-content: center;
  }
  .wrap-panel {
    display: block;
    width: 1125px;
    height: 488px;
  }
  .brand-name {
    font-family: "Montserrat", sans-serif;
    font-weight: 800;
    fill: var(--navy);
    letter-spacing: 2px;
  }
  .contact-text {
    font-family: "Montserrat", sans-serif;
    font-weight: 600;
    fill: var(--white);
  }
  .service-label {
    font-family: "Montserrat", sans-serif;
    font-weight: 500;
    font-size: 16px;
    fill: var(--white);
  }
  .icon-badge { fill: var(--orange); }
  .icon-line {
    stroke: var(--white);
    stroke-width: 2;
    fill: none;
    stroke-linecap: round;
    stroke-linejoin: round;
  }
</style>
</head>
<body>
<main class="canvas">
  <svg class="wrap-panel" viewBox="0 0 1430 620" xmlns="http://www.w3.org/2000/svg" aria-label="Brightwell Task Crew van side wrap">
    <!-- base panel -->
    <rect class="panel-base" x="0" y="0" width="1430" height="620" fill="var(--white)"/>

    <!-- navy body field -->
    <path class="navy-field" fill="var(--navy-deep)"
      d="M0,252 C200,238 380,282 472,352 L640,356 C770,215 960,22 1245,0 L1430,0 L1430,620 L0,620 Z"/>

    <!-- right sweep: navy hairline + orange stripe -->
    <path class="sweep-outline" fill="var(--navy)"
      d="M648,356 C790,205 975,28 1240,0 L1252,0 C990,34 800,214 660,356 Z"/>
    <path class="sweep-stripe" fill="var(--orange)"
      d="M632,356 C770,200 960,22 1235,0 L1180,0 C935,30 760,205 612,356 Z"/>

    <!-- left sweep: navy hairline + orange stripe -->
    <path class="sweep-outline" fill="var(--navy)"
      d="M0,205 C190,196 380,232 472,342 L466,343 C375,240 190,204 0,212 Z"/>
    <path class="sweep-stripe" fill="var(--orange)"
      d="M0,218 C195,205 370,245 455,344 L440,346 C360,265 195,245 0,250 Z"/>

    <!-- brand name -->
    <text class="brand-name" x="270" y="168" font-size="72">BRIGHTWELL</text>
    <text class="brand-name" x="272" y="222" font-size="40">TASK CREW</text>

    <!-- contact bands -->
    <rect class="contact-band" x="-20" y="332" width="412" height="40" rx="20" fill="var(--orange)"/>
    <rect class="contact-band" x="-20" y="382" width="412" height="38" rx="19" fill="var(--orange)"/>

    <g class="phone-icon" transform="translate(160,352)">
      <circle r="12" fill="none" stroke="var(--white)" stroke-width="1.6"/>
      <path d="M-5,-5 C-6,1 -1,6 5,5 L5,2 L2,1 L1,3 C-1,2 -2,1 -3,-1 L-1,-2 L-2,-5 Z" fill="var(--white)"/>
    </g>
    <text class="contact-text" x="366" y="362" font-size="27" text-anchor="end">555-014-2738</text>
    <text class="contact-text" x="366" y="409" font-size="19" text-anchor="end">www.brightwelltaskcrew.com</text>

    <!-- services -->
    <g class="service plumbing" transform="translate(683,410)">
      <circle class="icon-badge" r="14"/>
      <path class="icon-line" d="M-8,-2 L3,-2 L3,6 M-8,3 L-2,3 M-3,-6 L3,-6 M0,-6 L0,-2"/>
      <text class="service-label" x="20" y="6">Plumbing</text>
    </g>
    <g class="service handyman" transform="translate(683,446)">
      <circle class="icon-badge" r="14"/>
      <path class="icon-line" d="M-6,-6 L6,6 M6,-6 L-6,6"/>
      <text class="service-label" x="20" y="6">Handyman</text>
    </g>
    <g class="service land-management" transform="translate(828,412)">
      <circle class="icon-badge" r="14"/>
      <path class="icon-line" d="M-7,6 L7,6 M-5,6 L0,-6 L5,6 M-2,1 L2,1"/>
      <text class="service-label" x="20" y="6">Land Management</text>
    </g>
    <g class="service junk-removal" transform="translate(828,449)">
      <circle class="icon-badge" r="14"/>
      <path class="icon-line" d="M-6,-6 L6,6 M6,-6 L-6,6"/>
      <text class="service-label" x="20" y="6">Junk &amp; Debris Removal</text>
    </g>
  </svg>
</main>
</body>
</html>
```